Family Medicine Clinic Needs Mailchimp Newsletter Template

Looking for a responsive mailchimp template that matches the theme and overall look/feel of our website brightpathhc.com.

I'm looking for a professional, clean, simple, minimalist, bold design.
Colors would ideally be greens and blues, cool tones, muted colors, or graytones.

See attached word document for content for the upcoming newsletter

Can see prior newsletter content here:
http://brightpathhc.com/ourresources/newsletter-archive/

I have attached a copy of our brochure to see a sample of what we offer

The desired newsletter title would be:
The Bright Path
Looking for a great banner for that

Looking for basically 1 main photo area per text area for future templates

Under September is Comfort Outreach Month want links to our different services I mention

Under the videos section would like a video gallery of sorts that have links to the videos

Lumaderm image ad needs to be redone

Would like a button to take to schedule an appointment and patient portal
Easily visible phone number
Would like to have several sections with buttons to find out more

Would like feedback question at bottom
Rated 7-10 would forward to
https://zipqa.lnk/Rb8kWe

1-6 would send email to us

Reason: I have now guaranteed payment so I am giving a few more days for those designers that still want to submit a design

```html
<!DOCTYPE html>
<html lang="en">
<head>
<meta charset="utf-8">
<title>Bright Path Family Medicine – Feedback</title>
<link href="https://fonts.googleapis.com/css2?family=Open+Sans:wght@400;600;700&display=swap" rel="stylesheet">
<style>
  :root{
    --sky:#34a4d8;
    --sea:#2b7fae;
    --leaf:#7fad3b;
    --leaf-light:#8fbf45;
    --ink:#3a3a3a;
    --muted:#666;
    --social:#5e5e5e;
    --white:#fff;
    --frame:#d9d9d9;
  }
  *{box-sizing:border-box;margin:0;padding:0}
  html,body{width:1200px;height:1026px;overflow:hidden;background:var(--white)}
  body{font-family:"Open Sans",Arial,sans-serif;color:var(--ink);position:relative}

  .site-header{position:absolute;left:0;top:0;width:1200px;height:154px;border-top:4px solid var(--sky);background:var(--white)}
  .brand{position:absolute;display:flex;align-items:center;gap:10px;color:var(--sea)}
  .brand-dot{width:26px;height:26px;border-radius:50%;background:var(--sea)}
  .brand-text{font-weight:700;line-height:1}
  .brand-name{font-size:34px;display:block}
  .brand-sub{font-size:11px;letter-spacing:4.5px;display:block;margin-top:6px}
  .site-header .brand{left:76px;top:38px}

  .portal-tab{position:absolute;left:858px;top:0;width:270px;height:46px;background:var(--sea);
    clip-path:polygon(0 0,100% 0,93% 100%,7% 100%);color:var(--white);font-weight:700;font-size:15px;
    letter-spacing:.5px;display:flex;align-items:center;justify-content:center;gap:8px}
  .portal-tab svg{width:13px;height:13px}
  .btn-schedule{position:absolute;left:497px;top:61px;width:270px;height:45px;border-radius:23px;
    background:linear-gradient(var(--leaf-light),var(--leaf));color:var(--white);font-weight:700;font-size:14.5px;
    letter-spacing:.6px;display:flex;align-items:center;justify-content:center}
  .call-us{position:absolute;left:800px;top:68px;display:flex;align-items:center;gap:14px;font-size:17px;font-weight:600;color:var(--ink)}
  .call-us svg{width:20px;height:20px}
  .call-us .phone{color:var(--sea);font-size:24px;font-weight:700;margin-left:6px}

  .feedback{position:absolute;left:0;top:154px;width:1200px;height:646px;background:var(--sky);color:var(--white)}
  .feedback-title{position:absolute;top:38px;width:100%;text-align:center;font-size:34px;font-weight:700;letter-spacing:.5px}
  .feedback-question{position:absolute;top:98px;width:100%;text-align:center;font-size:14px}
  .scale{position:absolute;left:77px;top:161px;display:flex;gap:32.2px;list-style:none}
  .scale li{width:66px;height:66px;border:2px solid var(--white);border-radius:50%;display:flex;align-items:center;
    justify-content:center;font-size:34px;font-weight:400}
  .scale li.is-active{background:var(--leaf)}
  .scale-label{position:absolute;top:251px;font-size:16px}
  .scale-label.low{left:73px}
  .scale-label.high{right:73px}
  .team-photo{position:absolute;left:75px;top:315px;width:451px;height:275px;border:5px solid var(--frame);
    background:linear-gradient(135deg,#9c6a55,#6e4538 55%,#3a2a26)}
  .feedback-note{position:absolute;left:557px;top:311px;width:592px;font-size:14px;line-height:29.5px}

  .site-footer{position:absolute;left:0;top:800px;width:1200px;height:226px;text-align:center}
  .site-footer .brand{left:50%;transform:translateX(-50%);top:42px}
  .site-footer .brand-name{font-size:30px}
  .site-footer .brand-sub{font-size:10px;letter-spacing:4px}
  .copyright{position:absolute;top:117px;width:100%;font-size:14.5px;color:var(--muted)}
  .social{position:absolute;top:152px;left:50%;transform:translateX(-50%);display:flex;gap:14px;list-style:none;
    font-size:12px;font-weight:700;color:var(--social);white-space:nowrap}
</style>
</head>
<body>
  <header class="site-header">
    <div class="brand" aria-label="Bright Path Family Medicine">
      <span class="brand-dot"></span>
      <span class="brand-text"><span class="brand-name">Bright Path</span><span class="brand-sub">FAMILY MEDICINE</span></span>
    </div>
    <div class="portal-tab">
      <svg viewBox="0 0 16 16" fill="currentColor"><circle cx="8" cy="4.5" r="3.5"/><path d="M1 16c0-4 3-6.5 7-6.5s7 2.5 7 6.5z"/></svg>
      PATIENT PORTAL
    </div>
    <a class="btn-schedule">SCHEDULE AN APPOINTMENT</a>
    <div class="call-us">
      <svg viewBox="0 0 24 24" fill="#3a3a3a"><path d="M6.6 10.8a15 15 0 0 0 6.6 6.6l2.2-2.2c.3-.3.7-.4 1-.2 1.1.4 2.3.6 3.6.6.6 0 1 .4 1 1V20c0 .6-.4 1-1 1A17 17 0 0 1 3 4c0-.6.4-1 1-1h3.5c.6 0 1 .4 1 1 0 1.3.2 2.5.6 3.6.1.3 0 .7-.2 1z"/></svg>
      <span>CALL US NOW:<span class="phone">(555) 214-7830</span></span>
    </div>
  </header>

  <section class="feedback">
    <h1 class="feedback-title">Feedback Wanted</h1>
    <p class="feedback-question">How likely are you to recommend Bright Path Family Medicine to a friend or colleague?</p>
    <ol class="scale">
      <li class="is-active">0</li><li>1</li><li>2</li><li>3</li><li>4</li><li>5</li>
      <li>6</li><li>7</li><li>8</li><li>9</li><li>10</li>
    </ol>
    <span class="scale-label low">Not Likely</span>
    <span class="scale-label high">Extremely Likely</span>
    <div class="team-photo" role="img" aria-label="Group photo of the clinic team standing in front of a brick wall"></div>
    <p class="feedback-note">We value your feedback and strive to provide you with the best possible experience. If you have any suggestions on ways we can improve our care, please let us know. If we don't know there is a problem we can't fix it.</p>
  </section>

  <footer class="site-footer">
    <div class="brand" aria-label="Bright Path Family Medicine">
      <span class="brand-dot"></span>
      <span class="brand-text"><span class="brand-name">Bright Path</span><span class="brand-sub">FAMILY MEDICINE</span></span>
    </div>
    <p class="copyright">Copyright © 2017. Company Name. All Rights Reserved.</p>
    <ul class="social">
      <li>Share</li><li>Follow</li><li>Photos</li><li>Connect</li><li>Watch</li>
    </ul>
  </footer>
</body>
</html>
```